Plovanta medical teaching of the future

responsive website, onepager, for medical technology company. It has to look clean and high tech.

Look & feel
• Responsive
• Clean
• Combination icons + foto's
• Integration of a YouTube video

Landingpage items

• Header: picture + 'a video-based teaching platform for surgical procedures'
• About Deferred live medical teaching: Short description
• Features
o Video
o Teaching platform

• Benefits:
o More effective learning
o Faster sharing of knowledge & tecniques
o More cost effective

• References

• Products:
o Live (+link to more info)
o Qorvex (+ link to more info)
o Qorvex local (+link to more info)
o Qorvex cloud (+ link to more info)

• Solutions:
o For medical device companies (+link to more info)
o Doctor and surgeons (+link to more info)
o Medical conferences (+link to more info)

Target Market(s)

medical device companies
surgeons and doctors
conference organisers

Industry/Entity Type

It Company

Number of Pages Required

1 page

Requirements
Must have
• Landingpage items
• • Header: picture + 'a video-based teaching platform for surgical procedures'
• • About Deferred live medical teaching: Short description
• • Features
• o Video
• o Teaching platform
• • Benefits:
• o More effective learning
• o Faster sharing of knowledge & tecniques
• o More cost effective
• • References
• • Products:
• o Live (+link to more info)
• o Qorvex (+ link to more info)
• o Qorvex local (+link to more info)
• o Qorvex cloud (+ link to more info)
• • Solutions:
• o For medical device companies (+link to more info)
• o Doctor and surgeons (+link to more info)
• o Medical conferences (+link to more info)
Nice to have
• possibilty to show video

```html
<!DOCTYPE html>
<html lang="en">
<head>
<meta charset="utf-8">
<title>Plovanta – medical teaching of the future</title>
<link rel="stylesheet" href="https://fonts.googleapis.com/css2?family=Open+Sans:wght@400;600&family=Roboto:wght@400;500&display=swap">
<style>
:root{
  --teal:#3a9e98;
  --teal-dark:#2b7c77;
  --teal-deep:#0e3b3b;
  --aqua:#5fd6cc;
  --red:#e0001a;
  --red-dark:#a8001a;
  --grey:#a9a5a5;
  --grey-dark:#878383;
  --ink:#1d1d1d;
  --light:#efefef;
  --white:#fff;
}
*{box-sizing:border-box;margin:0;padding:0}
html,body{width:1200px;height:1200px;overflow:hidden;background:var(--white)}
body{position:relative;font-family:"Open Sans",sans-serif;color:var(--ink)}
.abs{position:absolute}
h1,h2,h3{font-family:"Roboto",sans-serif;font-weight:400}

/* hero */
.hero{left:0;top:0;width:1200px;height:370px;background:linear-gradient(120deg,#6aa7a6 0%,#4f8f92 35%,#8fb6b6 65%,#5e8f93 100%)}
.topbar{left:0;top:0;width:1200px;height:70px;background:rgba(120,130,130,.35)}
.brand{left:130px;top:0;width:249px;height:70px;background:var(--white);display:flex;align-items:center;gap:12px;padding-left:20px}
.brand-dot{width:34px;height:34px;border-radius:50%;background:var(--teal)}
.brand-name{font-family:"Roboto",sans-serif;font-size:32px;color:var(--teal);font-weight:500}
.nav a{position:absolute;top:24px;height:46px;line-height:46px;font-family:"Roboto",sans-serif;font-size:14px;color:var(--aqua);text-decoration:none}
.nav a.active{background:var(--aqua);color:var(--ink);padding:0 14px;font-weight:500}
.hero-title{left:132px;top:233px;width:556px;height:48px;background:rgba(120,140,140,.35);font-size:19.5px;color:var(--aqua);line-height:48px;text-align:center}
.hero-text{left:132px;top:286px;width:556px;height:76px;background:rgba(120,140,140,.35);font-family:"Roboto",sans-serif;font-size:13px;line-height:17.6px;color:var(--white);padding:8px 18px}
.video{background:linear-gradient(135deg,#5c8fa6,#3f6d7d);display:flex;align-items:center;justify-content:center}

/* about + features */
.about{left:0;top:370px;width:1200px;height:211px;background:var(--teal)}
.about svg{position:absolute;left:0;top:0}
.about-head{left:134px;top:74px;font-size:21px}
.rule{height:2px;width:45px;background:var(--teal)}
.about-text{left:134px;top:121px;width:300px;font-size:12px;line-height:16px;color:var(--white)}
.feat-head{left:534px;top:4px;font-size:19.5px;color:var(--ink)}
.feat-list{left:772px;top:52px;width:290px;list-style:none;font-size:12px;line-height:16px;color:var(--white)}
.feat-list li{position:relative;padding-left:25px;margin-bottom:8px}
.feat-list svg{position:absolute;left:0;top:1px}

/* benefits */
.sec-title{left:0;width:1200px;text-align:center;font-size:19.5px}
.sec-rule{left:577px;width:46px;height:2px;background:var(--teal)}
.benefit-sub{left:0;top:625px;width:1200px;text-align:center;font-family:"Roboto",sans-serif;font-size:11.5px;color:#333}
.card{top:654px;width:296px;height:158px;color:var(--white);overflow:hidden}
.card svg.foot{position:absolute;left:0;bottom:0}
.card .icon{position:absolute;left:14px;top:8px;width:84px;height:84px;border-radius:50%;display:flex;align-items:center;justify-content:center}
.card h3{position:absolute;left:109px;top:6px;width:180px;font-size:16px;line-height:16px;color:var(--ink)}
.card .u{position:absolute;left:109px;width:45px;height:2px;background:var(--ink)}
.card p{position:absolute;left:110px;width:182px;font-size:12px;line-height:16px}
.teal-c{background:var(--teal)} .teal-c .icon{background:var(--teal-dark)}
.red-c{background:var(--red)} .red-c .icon{background:var(--red-dark)}
.grey-c{background:var(--grey)} .grey-c .icon{background:var(--grey-dark)}

/* products */
.products{left:0;top:826px;width:1200px;height:169px;background:linear-gradient(90deg,#2f5b5c,#3e6e6c 50%,#2d5655)}
.prod{top:51px;width:215px;height:110px;background:rgba(150,165,165,.35)}
.prod .thumb{position:absolute;left:8px;top:8px;width:94px;height:94px;border-radius:50%;border:4px solid var(--aqua);background:linear-gradient(135deg,#6d9aa8,#3b6070)}
.prod .name{position:absolute;left:100px;right:0;top:26px;text-align:center;font-family:"Roboto",sans-serif;font-size:14px;color:var(--white)}
.btn{display:block;background:var(--aqua);color:#2c4a48;font-family:"Roboto",sans-serif;font-size:14px;text-align:center;text-decoration:none;line-height:37px;height:37px;width:95px}
.prod .btn{position:absolute;left:112px;top:66px}

/* solutions */
.solutions{left:0;top:995px;width:1200px;height:183px;background:var(--light)}
.sol-img{top:44px;width:296px;height:87px}
.sol-img span{position:absolute;left:6px;bottom:4px;color:var(--white);font-size:14px}
.sol-btn{top:139px}

.footer{left:0;top:1178px;width:1200px;height:22px;background:var(--teal-deep);color:var(--white);font-size:10px;text-align:center;line-height:22px}
</style>
</head>
<body>

<header class="abs hero" role="img" aria-label="Photo of surgeons operating in a theatre with monitors"></header>
<div class="abs topbar"></div>
<div class="abs brand"><span class="brand-dot"></span><span class="brand-name">Plovanta</span></div>
<nav class="nav">
  <a class="active" href="#" style="left:490px">Home</a>
  <a href="#" style="left:575px">About Us</a>
  <a href="#" style="left:665px">Features</a>
  <a href="#" style="left:752px">Benifits</a>
  <a href="#" style="left:832px">Products</a>
  <a href="#" style="left:920px">Solutions</a>
  <a href="#" style="left:1011px">Contact</a>
</nav>
<h1 class="abs hero-title">Plovanta changes the way medical procedures are taught.</h1>
<p class="abs hero-text">Plovanta is building a video based cloud teaching platform for all kinds of medical procedures using synchronized high resolution 360° and wide angle videos in a virtual reality environment.</p>
<div class="abs video" style="left:854px;top:225px;width:215px;height:137px" role="img" aria-label="Video still of a surgical team">
  <svg width="24" height="26" viewBox="0 0 24 26"><path d="M2 1 L23 13 L2 25Z" fill="#fff"/></svg>
</div>

<section class="abs about">
  <svg width="1200" height="211"><polygon points="0,0 444,0 494,211 0,211" fill="var(--grey)"/></svg>
  <svg class="abs" style="left:230px;top:11px" width="56" height="56" viewBox="0 0 56 56">
    <rect x="20" y="6" width="30" height="44" rx="2" fill="none" stroke="#fff" stroke-width="3"/>
    <rect x="29" y="2" width="12" height="7" fill="#fff"/>
    <path d="M6 16 L22 11 L38 16 V30 C38 42 22 50 22 50 C22 50 6 42 6 30Z" fill="#fff"/>
    <path d="M22 21 V37 M14 29 H30" stroke="var(--grey)" stroke-width="4"/>
    <path d="M40 22 H46 M40 30 H46 M40 38 H46" stroke="#fff" stroke-width="2.5"/>
  </svg>
  <h2 class="abs about-head">Deferred live medical teaching</h2>
  <div class="abs rule" style="left:134px;top:104px"></div>
  <p class="abs about-text">Healthcare companies contract top surgeons to do teaching sessions with their appliances/equipment. In the case of peer-to-peer medical teachings, medical device companies fly in surgeons from all over the world to attend live surgeries.</p>

  <h2 class="abs feat-head">Teaching Platform for medical procedures</h2>
  <div class="abs rule" style="left:534px;top:36px;background:var(--aqua)"></div>
  <div class="abs video" style="left:534px;top:54px;width:214px;height:134px" role="img" aria-label="Video still of an operating room">
    <svg width="22" height="24" viewBox="0 0 24 26"><path d="M2 1 L23 13 L2 25Z" fill="#fff"/></svg>
  </div>
  <ul class="abs feat-list">
    <li><svg width="16" height="17" viewBox="0 0 16 17"><path d="M8 1 L15 3.5 V8 C15 12 8 16 8 16 C8 16 1 12 1 8 V3.5Z" fill="none" stroke="var(--aqua)" stroke-width="1.5"/><path d="M4.5 8.5 L7 11 L11.5 6" fill="none" stroke="var(--aqua)" stroke-width="1.5"/></svg>Immersive cloud based teaching platform</li>
    <li><svg width="16" height="17" viewBox="0 0 16 17"><path d="M8 1 L15 3.5 V8 C15 12 8 16 8 16 C8 16 1 12 1 8 V3.5Z" fill="none" stroke="var(--aqua)" stroke-width="1.5"/><path d="M4.5 8.5 L7 11 L11.5 6" fill="none" stroke="var(--aqua)" stroke-width="1.5"/></svg>Based on high resolution wide-angle 360° video capturing of surgical procedures</li>
    <li><svg width="16" height="17" viewBox="0 0 16 17"><path d="M8 1 L15 3.5 V8 C15 12 8 16 8 16 C8 16 1 12 1 8 V3.5Z" fill="none" stroke="var(--aqua)" stroke-width="1.5"/><path d="M4.5 8.5 L7 11 L11.5 6" fill="none" stroke="var(--aqua)" stroke-width="1.5"/></svg>Multiple synchronized cameras</li>
    <li><svg width="16" height="17" viewBox="0 0 16 17"><path d="M8 1 L15 3.5 V8 C15 12 8 16 8 16 C8 16 1 12 1 8 V3.5Z" fill="none" stroke="var(--aqua)" stroke-width="1.5"/><path d="M4.5 8.5 L7 11 L11.5 6" fill="none" stroke="var(--aqua)" stroke-width="1.5"/></svg>A single person performs capturing with no need to access the OR</li>
  </ul>
</section>

<h2 class="abs sec-title" style="top:584px">Benefits</h2>
<div class="abs sec-rule" style="top:617px"></div>
<p class="abs benefit-sub">Medical and surgical knowledge can be shared in a faster, easier and more cost-effective way than current solutions like movies and pre-edited video.</p>

<article class="abs card teal-c" style="left:133px">
  <div class="icon"><svg width="48" height="46" viewBox="0 0 48 46"><rect x="4" y="4" width="40" height="30" fill="#fff"/><path d="M4 37 H44 M4 41 H44" stroke="#fff" stroke-width="2"/><path d="M24 8 V31 M17 13 H31" stroke="var(--teal-dark)" stroke-width="2"/><path d="M19 17 C29 19 19 23 29 25" fill="none" stroke="var(--teal-dark)" stroke-width="2"/></svg></div>
  <h3>More effective learning</h3><div class="u" style="top:30px"></div>
  <p style="top:38px">Easier learning due to advanced video-based interactivity and state of the art medical illustrations clarifying each step of the procedure</p>
  <svg class="foot" width="296" height="28"><polygon points="0,28 0,0 296,0 296,2" fill="var(--teal-dark)" transform="scale(1,-1) translate(0,-28)"/></svg>
</article>
<article class="abs card red-c" style="left:453px">
  <div class="icon"><svg width="56" height="60" viewBox="0 0 56 60"><g fill="none" stroke="#fff" stroke-width="3.5"><ellipse cx="28" cy="30" rx="25" ry="10"/><ellipse cx="28" cy="30" rx="25" ry="10" transform="rotate(60 28 30)"/><ellipse cx="28" cy="30" rx="25" ry="10" transform="rotate(-60 28 30)"/></g><circle cx="28" cy="30" r="4" fill="#fff"/></svg></div>
  <h3>Faster sharing of knowledge &amp; tecniques</h3><div class="u" style="top:46px"></div>
  <p style="top:54px">Faster sharing of knowledge and new techniques to surgeons worldwide due to the cloud-based teaching platform</p>
  <svg class="foot" width="296" height="28"><polygon points="0,28 0,0 296,0 296,2" fill="var(--red-dark)" transform="scale(1,-1) translate(0,-28)"/></svg>
</article>
<article class="abs card grey-c" style="left:773px">
  <div class="icon"><svg width="32" height="62" viewBox="0 0 32 62"><path d="M16 4 V50" stroke="#fff" stroke-width="5"/><path d="M27 16 C27 8 5 8 5 17 C5 27 27 24 27 35 C27 45 5 45 5 37" fill="none" stroke="#fff" stroke-width="5"/><path d="M6 48 L16 60 L26 48Z" fill="#fff"/></svg></div>
  <h3>More cost effective</h3><div class="u" style="top:30px"></div>
  <p style="top:38px">More cost-effective compared to traditional teaching methods</p>
  <svg class="foot" width="296" height="28"><polygon points="0,28 0,0 296,0 296,2" fill="var(--grey-dark)" transform="scale(1,-1) translate(0,-28)"/></svg>
</article>

<section class="abs products" role="img" aria-label="Dim teal background photo of an operating room">
  <h2 class="abs sec-title" style="top:9px;color:var(--white)">Products</h2>
  <div class="abs sec-rule" style="top:41px;background:var(--aqua)"></div>
  <div class="abs prod" style="left:134px"><div class="thumb" role="img" aria-label="Photo of capture hardware"></div><div class="name">Live</div><a class="btn" href="#">More Info</a></div>
  <div class="abs prod" style="left:374px"><div class="thumb" role="img" aria-label="Photo of surgical team"></div><div class="name">Qorvex</div><a class="btn" href="#">More Info</a></div>
  <div class="abs prod" style="left:614px"><div class="thumb" role="img" aria-label="Photo of operating room"></div><div class="name">Qorvex Local</div><a class="btn" href="#">More Info</a></div>
  <div class="abs prod" style="left:854px"><div class="thumb" role="img" aria-label="Photo of surgeon at work"></div><div class="name">Qorvex Cloud</div><a class="btn" href="#">More Info</a></div>
</section>

<section class="abs solutions">
  <h2 class="abs sec-title" style="top:2px">Solutions</h2>
  <div class="abs sec-rule" style="top:35px"></div>
  <div class="abs sol-img" style="left:133px;background:linear-gradient(90deg,#5a4e7a,#3c5e9a 60%,#7a8fb8)" role="img" aria-label="Photo of surgical video screens"><span>For Medical Device Companies</span></div>
  <div class="abs sol-img" style="left:453px;background:linear-gradient(90deg,#4c8580,#7a6a9a 45%,#3e7d84)" role="img" aria-label="Photo of surgeons watching a monitor"><span>Doctor and Surgeons</span></div>
  <div class="abs sol-img" style="left:773px;background:linear-gradient(90deg,#4a4a4a,#8d8d8d 45%,#3a3a3a)" role="img" aria-label="Photo of a medical conference hall"><span>Medical Conferences</span></div>
  <a class="abs btn sol-btn" href="#" style="left:237px">More Info</a>
  <a class="abs btn sol-btn" href="#" style="left:557px">More Info</a>
  <a class="abs btn sol-btn" href="#" style="left:877px">More Info</a>
</section>

<footer class="abs footer">Copyright@ Plovanta, 2017 | All Rights Reserved</footer>
</body>
</html>
```